Bref créative
Business Cards, Stationery and Email signature for Luxury Brand
Kestral
I need double sided standard sized Business Card [3.5" x 2"]
Can use whatever font will look high end
Professional
Dennis L. Farrow
CEO/President
417 Larkspur Ave.
Suite 350
Beverly Hills, CA 90187
df@kestralinquiries.example
kestralinquiries.example
Please put in holder for this - Don't have number yet
Want to have plastic business card. All black on front of card with just logo. Back of Card will have all information. Black border on back might be nice showing starburst from logo on top and having line under logo on bottom border of card. Open to other ideas for back as well.
ALL INFORMATION WILL GO ON BACK OF CARD - Card will be plastic
Logo only on front

```html
<!DOCTYPE html>
<html lang="en">
<head>
<meta charset="utf-8">
<title>Kestral – Business Card</title>
<link rel="stylesheet" href="https://fonts.googleapis.com/css2?family=Open+Sans:wght@400;600;700&display=swap">
<style>
  :root {
    --page: #ffffff;
    --card-black: #050505;
    --card-deep: #141414;
    --panel: #2a2a2a;
    --panel-light: #3a3a3a;
    --silver: #d6d6d6;
    --white: #f2f2f2;
    --gold: #e0a21c;
    --icon: #cfcfcf;
  }
  * { margin: 0; padding: 0; box-sizing: border-box; }
  html, body { width: 1200px; height: 901px; overflow: hidden; background: var(--page); }
  body { position: relative; font-family: "Open Sans", Arial, sans-serif; }

  .card {
    position: absolute;
    border-radius: 29px;
    overflow: hidden;
    box-shadow: 0 10px 22px rgba(0,0,0,0.35), 0 2px 5px rgba(0,0,0,0.25);
  }

  /* Front */
  .card-front {
    left: 115px; top: 77px; width: 545px; height: 309px;
    background: radial-gradient(ellipse at 51% 40%, #1d1d1d 0%, var(--card-black) 55%);
  }
  .brand-name {
    position: absolute;
    left: 0; right: 0;
    text-align: center;
    font-weight: 600;
    color: var(--silver);
    text-transform: uppercase;
  }
  .card-front .brand-name { top: 218px; font-size: 40px; letter-spacing: 6px; }

  /* Back */
  .card-back {
    left: 557px; top: 509px; width: 547px; height: 290px;
    background: linear-gradient(180deg, var(--card-deep), var(--card-black));
  }
  .back-panel { position: absolute; inset: 0; }
  .card-back .brand-name { left: 0; right: auto; width: 210px; top: 146px; font-size: 26px; letter-spacing: 3px; }

  .contact { position: absolute; left: 254px; top: 92px; color: var(--white); }
  .person-name { color: var(--gold); font-weight: 700; font-size: 15px; letter-spacing: 0.4px; line-height: 20px; }
  .person-role { font-weight: 600; font-size: 14px; line-height: 20px; margin-bottom: 10px; }
  .detail { display: flex; align-items: flex-start; font-size: 12.5px; line-height: 19px; }
  .detail svg { width: 12px; height: 12px; margin: 3px 7px 0 0; flex: none; }
  .detail-lines { display: flex; flex-direction: column; }
  .gap { margin-top: 14px; }
</style>
</head>
<body>

<section class="card card-front" aria-label="Card front">
  <div class="brand-name">Kestral</div>
</section>

<section class="card card-back" aria-label="Card back">
  <svg class="back-panel" viewBox="0 0 547 290" preserveAspectRatio="none" aria-hidden="true">
    <defs>
      <linearGradient id="panelShade" x1="0" y1="0" x2="1" y2="1">
        <stop offset="0" stop-color="#3c3c3c"/>
        <stop offset="1" stop-color="#1e1e1e"/>
      </linearGradient>
    </defs>
    <polygon points="163,0 547,0 547,290 134,290" fill="url(#panelShade)"/>
    <line x1="163" y1="0" x2="134" y2="290" stroke="#6a6a6a" stroke-width="1.5"/>
  </svg>

  <div class="brand-name">Kestral</div>

  <div class="contact">
    <div class="person-name">Dennis L. Farrow</div>
    <div class="person-role">CEO/President</div>

    <div class="detail">
      <svg viewBox="0 0 12 12"><circle cx="6" cy="6" r="6" fill="var(--icon)"/><path d="M3 6.3 6 3.5 9 6.3V9H3z" fill="#1a1a1a"/></svg>
      <div class="detail-lines">
        <span>417 Larkspur Ave.</span>
        <span>Suite 350</span>
        <span>Beverly Hills, CA 90187</span>
      </div>
    </div>

    <div class="detail gap">
      <svg viewBox="0 0 12 12"><circle cx="6" cy="6" r="5.4" fill="none" stroke="var(--icon)" stroke-width="1.2"/><path d="M4 3.5c.5 2.2 1.8 3.8 4 4.6l.4-.9-1.2-.7-.6.6C5.8 6.6 5.2 6 4.9 5.3l.6-.6-.6-1.3z" fill="var(--icon)"/></svg>
      <span>800-555-0142</span>
    </div>
    <div class="detail">
      <svg viewBox="0 0 12 12"><circle cx="6" cy="6" r="5.4" fill="none" stroke="var(--icon)" stroke-width="1.2"/><path d="M4 3.5c.5 2.2 1.8 3.8 4 4.6l.4-.9-1.2-.7-.6.6C5.8 6.6 5.2 6 4.9 5.3l.6-.6-.6-1.3z" fill="var(--icon)"/></svg>
      <span>310-555-0178</span>
    </div>
    <div class="detail">
      <svg viewBox="0 0 12 12"><circle cx="6" cy="6" r="5.4" fill="none" stroke="var(--icon)" stroke-width="1.2"/><rect x="3.2" y="4" width="5.6" height="4" fill="none" stroke="var(--icon)" stroke-width="0.9"/><path d="M3.2 4 6 6.2 8.8 4" fill="none" stroke="var(--icon)" stroke-width="0.9"/></svg>
      <span>df@kestralinquiries.example</span>
    </div>
    <div class="detail">
      <svg viewBox="0 0 12 12"><circle cx="6" cy="6" r="5.4" fill="none" stroke="var(--icon)" stroke-width="1.2"/><circle cx="6" cy="6" r="2.8" fill="none" stroke="var(--icon)" stroke-width="0.9"/><path d="M3.2 6h5.6M6 3.2v5.6" stroke="var(--icon)" stroke-width="0.8"/></svg>
      <span>www.kestralinquiries.example</span>
    </div>
  </div>
</section>

</body>
</html>
```